"Global Leadership & Talent Development Firm" needs a website upgrade

Website Design Project is intended to find a vendor to update and provide maintenance for my website: www.Brightpath2Growth.com. I am looking for a vendor who is an expert with WordPress and eCommerce plugin.

Website Requirements
www.Brightpath2Growth.com

• Media Library (review)- Add video/utube
• Others (plug-ins)
1) eCommerce ability
a) Must have the ability to charge for the eLearning courses
i) Handle credit card processing
ii) Ability to handle yearly subscriptions
iii) Ability to process credits/refunds

Website Updates Assessment Page:
• Complete TRAK- Distributor Information
• 7 Crew Habits Assessment & logo
• Stewardship Quest- 360 Assessment
• Emotional Intelligence Assessment
Home & Tool Pages:
• Q7Z License and certification
• CalmAxis Trainer
• 7 Crew Habits training
Client & Contact Pages
• Update Client list
• Update testimonials
Speaker Page Update
Website Add on E-Commerce to sell products
• Q7Z Certification Program
• CalmAxis tools & technology
• Complete TraK Assessment Distributor
• 7 Crew Habit Distributor

See attached document describing the updates.

Target Market(s)

Small-Large Business and Corporations
Public Sector Organizations

Industry/Entity Type

Leadership

Number of Pages Required

5+ page

Other font styles liked:
• www.brightpath2growth.com

Requirements
Must have
• Wordpress expertise
• E-Commerce plugin expertise
• Website Maintenance capability
Nice to have
• Easy access to transfer documents and get feedback/suggestions on the best wording for presenting the information onto my site for each of the pages
Should not have
• Focus on changing the current design of my site

```html
<!DOCTYPE html>
<html lang="en">
<head>
<meta charset="utf-8">
<title>Brightpath2Growth – Developing Leadership Talent &amp; Succession</title>
<link href="https://fonts.googleapis.com/css2?family=Arimo:wght@400;700&display=swap" rel="stylesheet">
<style>
  :root{
    --orange:#f0a035;
    --orange-dark:#e8921e;
    --ink:#222226;
    --text:#333338;
    --muted:#6b6b70;
    --band:#e4e4e9;
    --white:#ffffff;
    --footer:#0d0d12;
    --hero-a:#1c2430;
    --hero-b:#4a5868;
    --red:#cc3a30;
    --sky:#7ecbe2;
    --slate:#5a5a5c;
  }
  *{box-sizing:border-box;margin:0;padding:0}
  html,body{width:669px;height:1200px;overflow:hidden;background:var(--white)}
  body{position:relative;font-family:"Arimo",Arial,sans-serif;color:var(--text)}
  .abs{position:absolute}

  /* header */
  .brand{left:65px;top:17px;display:flex;align-items:center;gap:6px}
  .brand-mark{width:28px;height:28px;background:var(--orange);border-radius:3px}
  .brand-name{font-size:19px;color:var(--slate);letter-spacing:-.3px;line-height:1}
  .brand-tag{left:99px;top:48px;font-size:6.5px;color:var(--orange-dark)}

  .menu{left:491px;top:23px;width:116px;height:130px;background:var(--white);border:1px solid #c9c9d0;border-radius:4px;box-shadow:0 1px 3px rgba(0,0,0,.15);overflow:hidden;z-index:3}
  .menu-head{height:26px;background:var(--orange);display:flex;align-items:center;justify-content:space-between;padding-left:10px;color:var(--white);font-size:6.5px;font-weight:700}
  .menu-burger{width:16px;height:26px;background:var(--footer);display:flex;align-items:center;justify-content:center}
  .menu-item{height:25px;border-bottom:1px solid #eee;font-size:6.5px;color:var(--ink);display:flex;align-items:center;padding-left:10px}
  .menu-item:last-child{border-bottom:0}

  /* hero */
  .hero{left:0;top:74px;width:669px;height:325px;background:linear-gradient(120deg,var(--hero-a) 0%,var(--hero-b) 45%,#2a3440 70%,#5e6a74 100%)}
  .hero-arrow{top:226px;width:14px;height:20px}
  .caption{left:66px;top:246px;width:241px;height:126px;background:rgba(8,8,10,.92);border:2px solid #d8d8d8;border-radius:4px}
  .caption-close{position:absolute;right:9px;top:5px;color:var(--white);font-size:8px;font-weight:700}
  .caption-text{position:absolute;left:16px;top:12px;color:var(--white);font-size:19.5px;line-height:25px;letter-spacing:.3px}
  .caption-text strong{font-weight:700}
  .caption-btn{position:absolute;left:3px;top:99px;width:232px;height:21px;background:var(--orange-dark);color:var(--white);font-size:8px;font-weight:700;display:flex;align-items:center;padding-left:13px}
  .caption-btn span{margin-left:8px;font-size:9px}

  /* bands */
  .band-top{left:0;top:399px;width:669px;height:28px;background:var(--band)}
  .notch{width:0;height:0;border-left:8px solid transparent;border-right:8px solid transparent;border-top:7px solid var(--band)}

  /* approach */
  .section-title{left:0;width:669px;text-align:center;font-size:13.5px;font-weight:700;color:var(--ink);letter-spacing:.4px}
  .section-title em{font-style:normal;color:var(--orange-dark)}
  .approach-copy{left:84px;top:506px;width:502px;text-align:center;font-size:7.6px;line-height:13.5px;letter-spacing:.25px;color:var(--ink)}

  .tools{left:0;top:617px;width:669px;height:478px;background:var(--band)}
  .notch-white{left:327px;top:617px;border-top-color:var(--white)}

  /* tool cards */
  .tool{left:65px;width:543px;height:77px;background:var(--white);border-radius:4px}
  .tool-icon{position:absolute;left:0;top:0;width:55px;height:77px;border:2px solid #b9b9bf;border-radius:5px;display:flex;align-items:center;justify-content:center;background:#f2f2f4}
  .tool-icon .fill{position:absolute;inset:2px;border-radius:3px}
  .tool-icon svg{position:relative}
  .tool-body{position:absolute;left:76px;top:18px;right:20px}
  .tool-name{font-size:10.5px;color:var(--ink);letter-spacing:.3px;margin-bottom:2px}
  .tool-desc{font-size:7.6px;line-height:14.3px;letter-spacing:.25px;color:var(--ink)}

  /* footer */
  .footer{left:0;top:1095px;width:669px;height:105px;background:var(--footer)}
  .footer-nav{position:absolute;left:65px;right:61px;top:25px;display:flex;justify-content:space-between;font-size:9.5px;color:var(--white);letter-spacing:.3px}
  .footer-nav .current{font-weight:700}
  .footer-rule{position:absolute;left:65px;right:61px;top:58px;height:1px;background:#2a2a30}
  .footer-copy{position:absolute;left:0;right:0;top:80px;text-align:center;font-size:7.5px;color:#c8c8cc;letter-spacing:.4px}
  .footer-copy strong{color:var(--white)}
</style>
</head>
<body>

<header>
  <div class="abs brand"><div class="brand-mark"></div><div class="brand-name">Brightpath2Growth</div></div>
  <div class="abs brand-tag">Developing Leadership Talent &amp; Succession</div>

  <nav class="abs menu">
    <div class="menu-head">Menu
      <div class="menu-burger"><svg width="7" height="6" viewBox="0 0 7 6"><rect width="7" height="1.2" fill="#fff"/><rect y="2.4" width="7" height="1.2" fill="#fff"/><rect y="4.8" width="7" height="1.2" fill="#fff"/></svg></div>
    </div>
    <div class="menu-item">Coaching2Growth™</div>
    <div class="menu-item">Managing2Growth™</div>
    <div class="menu-item">Mentoring2Growth™</div>
    <div class="menu-item">Core Outlook Gauge™</div>
  </nav>
</header>

<section class="abs hero" role="img" aria-label="Photo of a businessman in a suit touching a glowing digital network of connected nodes"></section>
<svg class="abs hero-arrow" style="left:22px" viewBox="0 0 14 20"><path d="M11 2 3 10l8 8" fill="none" stroke="#fff" stroke-width="2"/></svg>
<svg class="abs hero-arrow" style="left:633px" viewBox="0 0 14 20"><path d="M3 2l8 8-8 8" fill="none" stroke="#fff" stroke-width="2"/></svg>

<div class="abs caption">
  <div class="caption-close">x</div>
  <p class="caption-text">Behind every<br>good result is a<br><strong>great insight.</strong></p>
  <div class="caption-btn">Learn More about Developing Leadership Talent<span>›</span></div>
</div>

<div class="abs band-top"></div>
<div class="abs notch" style="left:327px;top:427px"></div>

<h2 class="abs section-title" style="top:464px">Our <em>Approach</em></h2>
<p class="abs approach-copy">Looking for a boxed approach? You won't find it here. Our approach is an exchange; an exchange of dynamic listening and deliberate question asking. We ultimately identify the key leadership and talent factors that influence your organization's issues and successes. Then we apply our breadth of experience in working with companies like yours and people like you to develop a model of your company's leadership culture, language, symbols and values. As partners, we collaborate with you to mold, customize, and implement an application uniquely designed for your people, values, and systems, and strategies.</p>

<section class="abs tools"></section>
<div class="abs notch notch-white"></div>
<h2 class="abs section-title" style="top:648px;font-weight:700;color:#333">Tools</h2>

<article class="abs tool" style="top:688px">
  <div class="tool-icon"><div class="fill" style="background:var(--red)"></div>
    <svg width="34" height="30" viewBox="0 0 34 30"><g fill="#fff"><rect x="2" y="20" width="5" height="9" rx="1"/><rect x="10" y="15" width="5" height="14" rx="1"/><rect x="18" y="11" width="5" height="18" rx="1"/><rect x="26" y="7" width="5" height="22" rx="1"/><path d="M28.5 0l5 6h-10z"/></g></svg>
  </div>
  <div class="tool-body">
    <h3 class="tool-name">Coaching2Growth™</h3>
    <p class="tool-desc">Most leaders believe that setting ambitious goals and merely providing regular corrective feedback will create the results they need. Research and experience prove that this is NOT enough.</p>
  </div>
</article>

<article class="abs tool" style="top:785px">
  <div class="tool-icon"><div class="fill" style="background:var(--orange)"></div>
    <svg width="34" height="32" viewBox="0 0 34 32"><g fill="#fff"><path d="M17 0l2.6 5.6 6 .6-4.5 4 1.3 6L17 13.2 11.6 16.2l1.3-6-4.5-4 6-.6z"/><path d="M8 15l2.6 5.6 6 .6-4.5 4 1.3 6L8 28.2 2.6 31.2l1.3-6-4.5-4 6-.6z" transform="translate(1 0)"/><path d="M26 15l2.6 5.6 6 .6-4.5 4 1.3 6L26 28.2l-5.4 3 1.3-6-4.5-4 6-.6z" transform="translate(-1 0)"/></g></svg>
  </div>
  <div class="tool-body">
    <h3 class="tool-name">Managing2Growth™</h3>
    <p class="tool-desc">Management training must equip and empower managers to drive better results, make better decisions, and develop strong performers and teams. Enter Managing2Growth™, an intuitive and practical management model for managers and trainers.</p>
  </div>
</article>

<article class="abs tool" style="top:883px">
  <div class="tool-icon"><div class="fill" style="background:var(--sky)"></div>
    <svg width="36" height="26" viewBox="0 0 36 26"><g fill="#fff"><circle cx="7" cy="7" r="4"/><circle cx="29" cy="7" r="4"/><circle cx="18" cy="6" r="5"/><path d="M0 22c0-6 3-9 7-9s5 2 5 2v9H0z"/><path d="M36 22c0-6-3-9-7-9s-5 2-5 2v9h12z"/><path d="M9 26c0-8 4-12 9-12s9 4 9 12z"/></g></svg>
  </div>
  <div class="tool-body">
    <h3 class="tool-name">Mentoring2Growth™</h3>
    <p class="tool-desc">Research shows that employees entering the workplace today want work to afford them the opportunity to make new friends, learn new skills and connect to a larger purpose. That sense of purpose is a key factor in their job satisfaction and mentoring programs offer a vehicle to discover and confirm the purpose.</p>
  </div>
</article>

<article class="abs tool" style="top:981px">
  <div class="tool-icon"><div class="fill" style="background:linear-gradient(#8a8a8c,#3c3c3e)"></div>
    <svg width="34" height="34" viewBox="0 0 34 34"><g fill="#fff"><rect x="15.5" y="6" width="3" height="22"/><rect x="6" y="15.5" width="22" height="3"/><path d="M17 0l6 7H11z"/><path d="M17 34l6-7H11z"/><path d="M0 17l7-6v12z"/><path d="M34 17l-7-6v12z"/></g></svg>
  </div>
  <div class="tool-body">
    <h3 class="tool-name">Core Outlook Gauge®</h3>
    <p class="tool-desc">Achieving results is about closing gaps and turning strategy into execution and creativity into innovation. The bridge over these gaps is Collaboration. And the columns of this bridge are mind sets.</p>
  </div>
</article>

<footer class="abs footer">
  <nav class="footer-nav">
    <span class="current">Home</span><span>Approach</span><span>Tools</span><span>Assessments</span><span>Clients</span><span>Consultants</span><span>Speaking</span><span>Blog</span><span>Contact</span>
  </nav>
  <div class="footer-rule"></div>
  <p class="footer-copy">© <strong>Brightpath2Growth</strong>. All Rights Reserved</p>
</footer>

</body>
</html>
```